Redesign cement bags for leading cement producer in south east asia

We are from Larkfield cement and would like to redesign our bag to relaunch the product line. Our bags are made of high quality PP woven sack. We are one of the leading cement producers and we want our bags to have a Larkfield classy look on each visible side when it is loading in a truck or stacking on a pallet.

Thank you for interesting in this project. Good luck.

Project Deadline Extended Reason: Hi all, I have received requests to extend the deadline. Some of the work requires revising and some of them are still on process. To be fair, I also raise my budget to compensate the time. Thanks all for your participation. Added Sunday, July 10, 2016

Target Market(s)

Construction

Industry/Entity Type

Cement

Requirements
Must have
• You will have to design two bags for two cement grades. 52.5 is of higher grade and 42.5 is of lower grade. Both are similar in design but a distinctive colours to differentiate the two at once. Please look at Reference picture 2 for ideas.
Nice to have
• You do not have to change the original logo but the Larkfield cement word font changes are required. There are no restrictions to colours and font but please refrain from using feminine colours. Instructions on rear side of the bags are now included in the scope. Please create new layout and design new user friendly symbols.
Should not have
• Since cement is a dusty product, you need avoid some colours like black as background. The dust need to be less obvious to attract attention. Our previous base colour are shown in below.
• We want a fresh look on our bag, please do not just copy our old design and make small changes. I have attached our competitors' design, please refrain from using their design as well.
• It is recommend to do some research on cement bag sector.

```html
<!DOCTYPE html>
<html lang="en">
<head>
<meta charset="utf-8">
<title>Larkfield Cement – 52.5 Bag</title>
<link href="https://fonts.googleapis.com/css2?family=Open+Sans:wght@400;600;700;800&display=swap" rel="stylesheet">
<style>
  :root {
    --navy: #0f3a78;
    --white: #ffffff;
    --grey: #3a3a3a;
    --ink: #1e1e1e;
    --stage: #000000;
  }
  * { margin: 0; padding: 0; box-sizing: border-box; }
  html, body { width: 1200px; height: 960px; overflow: hidden; background: var(--stage); }
  body { font-family: "Open Sans", sans-serif; color: var(--ink); }
  .canvas { position: relative; width: 1200px; height: 960px; }
  .bag { position: absolute; left: 111px; top: 74px; width: 999px; height: 800px; background: var(--white); overflow: hidden; }
  .abs { position: absolute; }
  .band { position: absolute; background: var(--navy); }
  .band-top { left: 0; top: 21px; width: 999px; height: 49px; }
  .band-bottom { left: 0; top: 724px; width: 999px; height: 49px; }
  .grade-line { position: absolute; color: var(--white); font-weight: 600; font-size: 22px; white-space: nowrap; line-height: 1; }
  .grade-line b { font-size: 30px; font-weight: 700; }
  .grade-top { left: 28px; top: 33px; transform: rotate(180deg); }
  .grade-bottom { left: 537px; top: 738px; }

  .front-blue { left: 0; top: 207px; width: 399px; height: 257px; background: var(--navy); }
  .back-blue { left: 399px; top: 100px; width: 600px; height: 304px; background: var(--navy); }
  .info-box { left: 499px; top: 202px; width: 400px; height: 522px; background: var(--white); }

  .spec { left: 0; width: 399px; text-align: center; font-size: 14px; color: var(--grey); line-height: 20px; }
  .mark-dot { position: absolute; border-radius: 50%; background: var(--white); }
  .mark-dot.navy { background: var(--navy); }
  .brand-name { position: absolute; font-weight: 800; color: var(--white); line-height: 1; white-space: nowrap; letter-spacing: 1px; }
  .brand-sub { position: absolute; font-weight: 700; color: var(--grey); line-height: 1; white-space: nowrap; }
  .front-name { left: 0; width: 399px; text-align: center; top: 416px; font-size: 58px; }
  .front-sub { left: 0; width: 399px; text-align: center; top: 488px; font-size: 36px; }
  .origin { left: 0; width: 399px; text-align: center; top: 572px; color: var(--navy); font-weight: 600; font-size: 19px; line-height: 24px; }
  .weight { left: 0; width: 399px; text-align: center; top: 644px; font-size: 13px; color: var(--grey); }

  .back-name { right: 120px; top: 161px; font-size: 46px; }
  .back-sub { right: 120px; top: 209px; font-size: 30px; }

  .side-up { position: absolute; writing-mode: vertical-rl; font-weight: 800; line-height: 1; white-space: nowrap; }
  .side-down { position: absolute; writing-mode: vertical-rl; transform: rotate(180deg); font-weight: 800; line-height: 1; white-space: nowrap; }
  .side-lg { font-size: 30px; }
  .side-sm { font-size: 22px; font-weight: 700; }
  .on-navy { color: var(--white); }
  .on-white { color: var(--navy); }
  .on-white.sub { color: var(--grey); }

  .content { left: 524px; top: 0; width: 370px; }
  .h { position: absolute; left: 0; font-weight: 700; font-size: 12.5px; letter-spacing: .2px; white-space: nowrap; }
  .p { position: absolute; left: 0; font-size: 9.5px; white-space: nowrap; }
  .small { font-size: 7.5px; }

  .mix-table { position: absolute; left: 523px; top: 307px; border-collapse: collapse; font-size: 7.5px; }
  .mix-table td, .mix-table th { border: 1px solid var(--ink); font-weight: 400; padding: 0 8px; }
  .mix-table th { height: 16px; text-align: center; }
  .mix-table th:first-child, .mix-table td:first-child { text-align: left; }
  .mix-table td { height: 23px; text-align: center; }
  .barrow { display: inline-block; width: 7px; height: 4px; margin: 0 1px; background: var(--grey); border-radius: 0 0 4px 4px; }

  .precaution { position: absolute; left: 0; font-size: 8.5px; white-space: nowrap; line-height: 10px; }
  .precaution svg { position: absolute; left: -22px; top: -1px; }
  .maker { font-weight: 700; font-size: 7.5px; }
  .maker-name { color: var(--navy); font-weight: 700; font-size: 12px; }
  .maker-name small { font-size: 9px; }
</style>
</head>
<body>
<div class="canvas">
  <div class="bag">
    <div class="band band-top"></div>
    <div class="grade-line grade-top">Exort Quality <b>52.5</b> Cement</div>

    <div class="abs front-blue"></div>
    <div class="abs back-blue"></div>
    <div class="abs info-box"></div>

    <!-- front face -->
    <div class="abs spec" style="top:139px;">Portland Cement<br>En 197-1 (2000), Strength Class 52.5</div>
    <div class="mark-dot" style="left:151px; top:262px; width:90px; height:90px;"></div>
    <div class="brand-name front-name">LARKFIELD</div>
    <div class="brand-sub front-sub">CEMENT</div>
    <div class="abs origin">Export Quality<br>Product of Myanmar</div>
    <div class="abs weight">Net Weight 50Kg</div>

    <!-- back face header -->
    <div class="mark-dot" style="left:518px; top:118px; width:74px; height:74px;"></div>
    <div class="brand-name back-name">LARKFIELD</div>
    <div class="brand-sub back-sub">CEMENT</div>

    <!-- left gusset -->
    <div class="mark-dot" style="left:424px; top:116px; width:60px; height:60px;"></div>
    <div class="side-up on-navy side-lg" style="left:454px; top:200px;">LARKFIELD</div>
    <div class="side-up on-navy side-sm" style="left:422px; top:262px;">CEMENT</div>
    <div class="side-down on-white side-lg" style="left:423px; top:424px;">LARKFIELD</div>
    <div class="side-down on-white sub side-sm" style="left:465px; top:428px;">CEMENT</div>
    <div class="mark-dot navy" style="left:411px; top:620px; width:60px; height:60px;"></div>

    <!-- right gusset -->
    <div class="mark-dot" style="left:924px; top:116px; width:60px; height:60px;"></div>
    <div class="side-up on-navy side-lg" style="left:954px; top:200px;">LARKFIELD</div>
    <div class="side-up on-navy side-sm" style="left:922px; top:262px;">CEMENT</div>
    <div class="side-down on-white side-lg" style="left:923px; top:424px;">LARKFIELD</div>
    <div class="side-down on-white sub side-sm" style="left:965px; top:428px;">CEMENT</div>
    <div class="mark-dot navy" style="left:911px; top:620px; width:60px; height:60px;"></div>

    <!-- instructions -->
    <div class="abs content">
      <div class="h" style="top:229px;">APPLICATION</div>
      <div class="p" style="top:254px;">Suitable for general concrete products.</div>
      <div class="h" style="top:285px;">MIXING INSTRUCTIONS</div>
      <div class="h" style="top:389px;">RECOMMENDATION</div>
      <div class="p small" style="top:411px;">During 1-3 days of curing process, concrete should be sprayed with water to avoid crack.</div>
      <div class="p small" style="top:426px;">A bag of cement should be finished within 1day. If not seal the bag tightly</div>
      <div class="h" style="top:455px;">PRECAUTIONS</div>
    </div>

    <table class="mix-table">
      <tr><th>Applications</th><th>Cement</th><th>Sand</th><th>Aggregate</th><th>Water</th></tr>
      <tr>
        <td style="width:94px;">Lean Concrete</td>
        <td style="width:52px;"><span class="barrow"></span></td>
        <td style="width:46px;"><span class="barrow"></span><span class="barrow"></span><span class="barrow"></span></td>
        <td style="width:61px;"><span class="barrow"></span><span class="barrow"></span><span class="barrow"></span><br><span class="barrow"></span><span class="barrow"></span></td>
        <td style="width:47px;"><span class="barrow"></span></td>
      </tr>
      <tr>
        <td>General Concrete</td>
        <td><span class="barrow"></span></td>
        <td><span class="barrow"></span><span class="barrow"></span></td>
        <td><span class="barrow"></span><span class="barrow"></span><span class="barrow"></span><span class="barrow"></span></td>
        <td><span class="barrow"></span></td>
      </tr>
    </table>

    <div class="abs" style="left:543px; top:0; width:350px;">
      <div class="precaution" style="top:477px;"><svg width="13" height="13" viewBox="0 0 13 13"><circle cx="6.5" cy="6.5" r="6.5" fill="var(--navy)"/><rect x="4" y="4" width="5" height="5" fill="#fff"/></svg>Lift with care.</div>
      <div class="precaution" style="top:496px;"><svg width="13" height="13" viewBox="0 0 13 13"><circle cx="6.5" cy="6.5" r="6.5" fill="var(--navy)"/><rect x="4.5" y="3.5" width="4" height="6" rx="1.5" fill="#fff"/></svg>Wear gloves while mixing or handling dry cement.</div>
      <div class="precaution" style="top:516px;"><svg width="13" height="13" viewBox="0 0 13 13"><circle cx="6.5" cy="6.5" r="6.5" fill="var(--navy)"/><rect x="3.5" y="5" width="6" height="3.5" rx="1.5" fill="#fff"/></svg>Wear a mask while mixing dry cement.</div>
      <div class="precaution" style="top:535px;"><svg width="13" height="13" viewBox="0 0 13 13"><circle cx="6.5" cy="6.5" r="6.5" fill="var(--navy)"/><circle cx="6.5" cy="4.5" r="1.6" fill="#fff"/><rect x="5" y="6.5" width="3" height="3.5" fill="#fff"/></svg>Keep cement away from child's reach.</div>
      <div class="precaution" style="top:555px;"><svg width="13" height="13" viewBox="0 0 13 13"><circle cx="6.5" cy="6.5" r="6.5" fill="var(--navy)"/><path d="M3 7 A3.5 3.5 0 0 1 10 7 Z" fill="#fff"/><rect x="6" y="7" width="1" height="3" fill="#fff"/></svg>Cement should be stored under shade and away from<br>moisture with pallats being raised above ground.</div>
    </div>

    <div class="abs" style="left:522px; top:0; width:370px;">
      <div class="p maker" style="top:598px;">Manufactured and distributed by:</div>
      <div class="p maker-name" style="top:609px;">TAMARIND RIDGE <small>CEMENT CO.,LTD.</small></div>
      <div class="p" style="top:635px; font-size:7px;">No.48, 12th Street, Between 20th and 21st Streets Riverside Township Mandalay, Myanmar</div>
      <div class="p" style="top:650px; font-size:7px;">Tel : (95)2 40110, (95)2 40120, (95)3 50130, (95)2 40140, (95)2 40150, (95)2 40160</div>
      <div class="p" style="top:665px; font-size:7px;">Fax : (95)2 40170,&nbsp;&nbsp; Email: sales@tamarindridge.example,&nbsp;&nbsp; www.tamarindridge.example</div>
    </div>

    <div class="band band-bottom"></div>
    <div class="grade-line grade-bottom">Exort Quality <b>52.5</b> Cement</div>
  </div>
</div>
</body>
</html>
```